INTERNATIONAL COMPANY IN MARITIME AIR TRANSPORT AND LOGISTICS

We need a power point model with the attached logo, we organize the transport of goods around the world by plane and boat. We also organize logistics. We would like a creation in the colors of our logo or in agreement with this one. The final design must convey the openness to international, men at the heart of our service and the strength of our company.

Target Market(s)

LUX - Aeronautics - RETAIL

Industry/Entity Type

Retail

Font styles to use
Serif

Colors

Designer to choose colors to be used in the design.

Requirements
Must have
• We need a power point model with the attached logo, we organize the transport of goods around the world by plane and boat. We also organize logistics. We would like a creation in the colors of our logo or in agreement with this one. The final design must convey the openness to international, men at the heart of our service and the strength of our company.
Nice to have
Should not have
• FREE

```html
<!DOCTYPE html>
<html lang="en">
<head>
<meta charset="utf-8">
<title>Meridex Presentation Template</title>
<link href="https://fonts.googleapis.com/css2?family=Arimo:wght@400;700&family=Open+Sans:wght@400;600;700&display=swap" rel="stylesheet">
<style>
:root{
  --cyan:#29b5e8;
  --cyan-deep:#1a9fd6;
  --cyan-light:#bfe8f8;
  --sky:#e3f5fc;
  --slate:#4b5664;
  --rule:#3f4c5a;
  --ink:#111418;
  --grey:#5f6670;
  --soft-grey:#efeff0;
  --canvas:#dddddd;
  --navy:#1e5ba8;
}
*{box-sizing:border-box}
html,body{margin:0;padding:0}
body{width:1200px;height:1150px;overflow:hidden;background:var(--canvas);position:relative;font-family:'Arimo',Arial,sans-serif;color:var(--ink)}
.slide{position:absolute;width:626px;height:352px;background:#fff;transform:scale(.6125);transform-origin:0 0;overflow:hidden;border-bottom:3px solid var(--rule)}
.c1{left:15px}.c2{left:410px}.c3{left:805px}
.r1{top:12px}.r2{top:239px}.r3{top:465px}.r4{top:692px}.r5{top:918px}
.abs{position:absolute}
.head-rule{position:absolute;top:14px;left:0;right:0;height:1px;background:var(--cyan)}
.tab{position:absolute;top:0;right:14px;width:17px;height:38px;background:var(--cyan);border-radius:0 0 6px 6px}
.mark{position:absolute;top:20px;right:36px;display:flex;align-items:center;gap:3px;font-size:7px;font-weight:700;letter-spacing:1px;color:var(--slate)}
.mark i{display:block;width:6px;height:6px;background:var(--cyan)}
.brand{display:flex;align-items:center;gap:10px;font-family:'Open Sans',Arial,sans-serif;font-weight:400;letter-spacing:4px;color:#fff}
.brand i{display:block;background:#fff}
.title{position:absolute;left:0;right:0;text-align:center;font-weight:700;font-size:22px;color:var(--ink)}
.photo{position:absolute}
.small{font-size:6.5px;line-height:1.45;color:var(--grey)}
.just{text-align:justify}
.label{font-size:7.5px;font-weight:700;color:var(--ink)}
.cyan-head{background:var(--cyan);color:#fff;font-size:7.5px;font-weight:700;text-align:center;padding:5px 0}
.grey-box{background:var(--soft-grey);padding:8px 12px}
</style>
</head>
<body>

<!-- 1 Title -->
<section class="slide c1 r1">
  <svg class="abs" style="left:0;top:0" width="626" height="352" role="img" aria-label="Cargo ship and aircraft at a port in sunset light">
    <defs>
      <linearGradient id="sunset" x1="0" y1="0" x2="0" y2="1">
        <stop offset="0" stop-color="#6b4a2a"/><stop offset=".45" stop-color="#b8743a"/><stop offset="1" stop-color="#7a3d2a"/>
      </linearGradient>
    </defs>
    <path d="M8 8 H345 C200 70 180 260 420 346 H8 Z" fill="url(#sunset)"/>
    <path d="M350 8 C200 72 185 262 428 346" fill="none" stroke="#fff" stroke-width="12"/>
    <path d="M250 8 C160 90 160 260 290 346" fill="none" stroke="#fff" stroke-width="4"/>
    <path d="M205 8 C130 110 140 270 225 346" fill="none" stroke="#fff" stroke-width="3"/>
  </svg>
  <div class="abs" style="left:16px;top:176px">
    <div class="brand" style="font-size:24px"><i style="width:14px;height:14px"></i>MERIDEX</div>
  </div>
  <div class="abs" style="left:275px;top:148px;font-size:28px;font-weight:700;color:#5a5a5a;letter-spacing:1px">PRESENTATION TITLE</div>
  <div class="abs" style="left:357px;top:188px;font-size:18px;color:#3b6e8f">Sub title goes here</div>
</section>

<!-- 2 Title alt -->
<section class="slide c2 r1">
  <div class="photo" role="img" aria-label="Port at dusk with a world route map overlay" style="left:0;top:0;width:626px;height:258px;background:linear-gradient(180deg,#2b6fb3 0%,#5a9bd0 45%,#c9a36a 80%,#3a5f8a 100%)"></div>
  <div class="abs" style="left:30px;top:26px;width:566px;height:214px;border-radius:30px;background:rgba(235,244,252,.72)"></div>
  <div class="abs" style="left:0;right:0;top:100px;text-align:center;font-size:34px;font-weight:700;color:var(--navy);letter-spacing:1px">PRESENTATION TITLE</div>
  <div class="abs" style="left:0;right:0;top:142px;text-align:center;font-size:22px;color:var(--navy)">Sub title goes here</div>
  <div class="abs" style="left:242px;top:298px">
    <div class="brand" style="font-size:20px;color:var(--slate)"><i style="width:12px;height:12px;background:var(--cyan)"></i>MERIDEX</div>
  </div>
</section>

<!-- 3 Agenda -->
<section class="slide c3 r1">
  <div class="head-rule"></div><div class="tab"></div><div class="mark"><i></i>MERIDEX</div>
  <div class="abs" style="left:262px;top:22px;font-size:28px;font-weight:700">Agenda</div>
  <div class="photo" role="img" aria-label="Business handshake in blue tone" style="left:0;top:72px;width:328px;height:220px;background:linear-gradient(135deg,#1e8fd0,#4cc0ee 60%,#2aa6df)"></div>
  <div class="abs" style="left:40px;top:164px">
    <div class="brand" style="font-size:30px"><i style="width:16px;height:16px"></i>MERIDEX</div>
  </div>
  <svg class="abs" style="left:400px;top:60px" width="220" height="290">
    <line x1="8" y1="0" x2="8" y2="290" stroke="#cfd6dc" stroke-width="1.5"/>
    <g fill="#fff" stroke="var(--cyan)" stroke-width="2">
      <circle cx="8" cy="15" r="4"/><circle cx="8" cy="56" r="4"/><circle cx="8" cy="97" r="4"/>
      <circle cx="8" cy="138" r="4"/><circle cx="8" cy="179" r="4"/><circle cx="8" cy="220" r="4"/>
    </g>
    <g font-family="Open Sans,Arial,sans-serif" font-size="10" font-weight="600" fill="#3d5467">
      <text x="22" y="19">Mission &amp; Vision</text><text x="22" y="60">Our Services</text>
      <text x="22" y="101">Company Profile</text><text x="22" y="142">Project Portfolio</text>
      <text x="22" y="183">Our Team</text><text x="22" y="224">Q&amp;As / Closing Speech</text>
    </g>
  </svg>
</section>

<!-- 4 Company profile -->
<section class="slide c1 r2">
  <div class="head-rule"></div><div class="tab"></div><div class="mark"><i></i>MERIDEX</div>
  <div class="abs" style="left:38px;top:310px;transform:rotate(-90deg);transform-origin:0 0;font-size:24px;font-weight:700;color:var(--cyan);white-space:nowrap">COMPANY PROFILE</div>
  <div class="photo" role="img" aria-label="Warehouse loading docks in blue tone" style="left:73px;top:42px;width:260px;height:283px;background:linear-gradient(180deg,#2595cc,#5cc3ec 60%,#a8e0f5)"></div>
  <div class="abs" style="left:95px;top:168px">
    <div class="brand" style="font-size:26px"><i style="width:15px;height:15px"></i>MERIDEX</div>
  </div>
  <div class="abs" style="left:333px;top:42px;width:280px;height:283px;background:var(--slate);padding:46px 26px;color:#fff;font-size:8px;line-height:1.55;text-align:justify">
    <p style="margin:0 0 14px">Lorem ipsum dolor sit amet, consectetur adipiscing elit, sed do eiusmod tempor incididunt ut labore et dolore magna aliqua. Lorem ipsum dolor sit amet, consectetur adipiscing elit, sed do eiusmod tempor incididunt ut labore et dolore magna aliqua. Ut enim ad minim veniam, quis nostrud exercitation ullamco laboris nisi ut aliquip.</p>
    <p style="margin:0">Lorem ipsum dolor sit amet, consectetur adipiscing elit, sed do eiusmod tempor incididunt ut labore et dolore magna aliqua. Lorem ipsum dolor sit amet, consectetur adipiscing elit, sed do eiusmod tempor incididunt ut labore et dolore magna aliqua.</p>
  </div>
</section>

<!-- 5 Four columns over port -->
<section class="slide c2 r2">
  <div class="head-rule"></div><div class="tab"></div><div class="mark"><i></i>MERIDEX</div>
  <div class="title" style="top:36px">Lorem ipsum dolor sit amet</div>
  <div class="photo" role="img" aria-label="Container port with crane, ship and aircraft" style="left:0;top:172px;width:626px;height:180px;background:linear-gradient(180deg,#bfe6f7,#6cc6ee 55%,#2ea9df)"></div>
  <div class="abs small" style="left:22px;top:82px;width:125px;text-align:center"><div class="label">Your Contents Here</div>Lorem ipsum dolor sit amet, consectetur adipiscing elit, sed do eiusmod tempor incididunt ut labore et dolore magna aliqua. Lorem ipsum dolor sit amet, consectetur adipiscing elit.</div>
  <div class="abs small" style="left:158px;top:82px;width:125px;text-align:center"><div class="label">Your Contents Here</div>Lorem ipsum dolor sit amet, consectetur adipiscing elit, sed do eiusmod tempor incididunt ut labore et dolore magna aliqua. Lorem ipsum dolor sit amet, consectetur adipiscing elit.</div>
  <div class="abs small" style="left:300px;top:75px;width:140px;height:136px;background:var(--cyan);color:#fff;text-align:center;padding:30px 10px 0"><div class="label" style="color:#fff">Your Contents Here</div>Lorem ipsum dolor sit amet, consectetur adipiscing elit, sed do eiusmod tempor incididunt ut labore et dolore magna aliqua. Lorem ipsum dolor sit amet, consectetur adipiscing elit.</div>
  <div class="abs small" style="left:458px;top:82px;width:125px;text-align:center"><div class="label">Your Contents Here</div>Lorem ipsum dolor sit amet, consectetur adipiscing elit, sed do eiusmod tempor incididunt ut labore et dolore magna aliqua. Lorem ipsum dolor sit amet, consectetur adipiscing elit.</div>
</section>

<!-- 6 Four boxes -->
<section class="slide c3 r2">
  <div class="head-rule" style="left:215px"></div><div class="tab"></div><div class="mark"><i></i>MERIDEX</div>
  <div class="photo" role="img" aria-label="Globe held in a ring of paper people" style="left:0;top:0;width:215px;height:352px;background:radial-gradient(circle at 55% 45%,#8fb8e8,#3f6fb0 45%,#dbe6f3 80%)"></div>
  <div class="abs" style="left:262px;top:50px;font-size:22px;font-weight:700">Lorem ipsum dolor sit amet</div>
  <div class="abs" style="left:273px;top:95px;width:137px"><div class="cyan-head">Your Contents Here</div><div class="grey-box small just" style="height:93px">Lorem ipsum dolor sit amet, consectetur adipiscing elit, sed do eiusmod tempor incididunt ut labore et dolore magna aliqua. Lorem ipsum dolor sit amet, consectetur adipiscing elit.</div></div>
  <div class="abs" style="left:420px;top:95px;width:137px"><div class="cyan-head">Your Contents Here</div><div class="grey-box small just" style="height:93px">Lorem ipsum dolor sit amet, consectetur adipiscing elit, sed do eiusmod tempor incididunt ut labore et dolore magna aliqua. Lorem ipsum dolor sit amet, consectetur adipiscing elit.</div></div>
  <div class="abs" style="left:273px;top:214px;width:137px"><div class="cyan-head">Your Contents Here</div><div class="grey-box small just" style="height:93px">Lorem ipsum dolor sit amet, consectetur adipiscing elit, sed do eiusmod tempor incididunt ut labore et dolore magna aliqua. Lorem ipsum dolor sit amet, consectetur adipiscing elit.</div></div>
  <div class="abs" style="left:420px;top:214px;width:137px"><div class="cyan-head">Your Contents Here</div><div class="grey-box small just" style="height:93px">Lorem ipsum dolor sit amet, consectetur adipiscing elit, sed do eiusmod tempor incididunt ut labore et dolore magna aliqua. Lorem ipsum dolor sit amet, consectetur adipiscing elit.</div></div>
</section>

<!-- 7 Containers with chart -->
<section class="slide c1 r3">
  <div class="photo" role="img" aria-label="Stacked shipping containers under a blue sky" style="left:0;top:0;width:626px;height:352px;background:linear-gradient(180deg,#d8ecf7 0%,#c9a25a 40%,#8d9a6a 65%,#6fb6cf 100%)"></div>
  <div class="abs" style="left:83px;top:86px;font-size:33px;font-weight:700">Lorem ipsum dolor sit amet</div>
  <div class="abs" style="left:18px;top:180px;width:594px;height:160px;background:rgba(76,180,230,.72)"></div>
  <div class="abs just" style="left:38px;top:188px;width:292px;font-size:7.5px;line-height:1.45;color:#fff">Experimental finance aims to establish different market settings and environments to observe experimentally and provide a lens through which science can analyze agents' behavior and the resulting characteristics of trading flows, information diffusion and aggregation, price setting mechanisms, and returns processes. Researchers in experimental finance can study to what extent existing financial economics theory makes valid predictions and therefore prove them, and attempt to discover new principles on which such theory can be extended and be applied to future financial decisions. Research may proceed by conducting trading simulations or by establishing and studying the behavior, and the way that these people act or react.</div>
  <svg class="abs" style="left:360px;top:186px" width="240" height="150">
    <g stroke="rgba(255,255,255,.5)" stroke-width=".5"><line x1="10" y1="20" x2="235" y2="20"/><line x1="10" y1="55" x2="235" y2="55"/><line x1="10" y1="90" x2="235" y2="90"/><line x1="10" y1="120" x2="235" y2="120"/></g>
    <g fill="#fff"><rect x="30" y="75" width="8" height="45"/><rect x="82" y="50" width="8" height="70"/><rect x="134" y="30" width="8" height="90"/><rect x="186" y="40" width="8" height="80"/></g>
    <g fill="#c8ecfb"><rect x="40" y="60" width="8" height="60"/><rect x="92" y="35" width="8" height="85"/><rect x="144" y="55" width="8" height="65"/><rect x="196" y="30" width="8" height="90"/></g>
    <g fill="#2c9bd6"><rect x="50" y="85" width="8" height="35"/><rect x="102" y="20" width="8" height="100"/><rect x="154" y="40" width="8" height="80"/><rect x="206" y="45" width="8" height="75"/></g>
    <g font-size="5" fill="#fff"><text x="28" y="130">Category 1</text><text x="80" y="130">Category 2</text><text x="132" y="130">Category 3</text><text x="184" y="130">Category 4</text><text x="70" y="142">■ Series 1  ■ Series 2  ■ Series 3</text></g>
  </svg>
</section>

<!-- 8 Global delivery -->
<section class="slide c2 r3">
  <div class="head-rule"></div><div class="tab"></div><div class="mark"><i></i>MERIDEX</div>
  <div class="title" style="top:40px">Global Delivery</div>
  <div class="abs small" style="left:150px;top:92px;width:120px;text-align:center"><div class="label">Your Contents Here</div>Lorem ipsum dolor sit amet, consectetur adipiscing elit, sed do eiusmod tempor incididunt ut labore et dolore magna aliqua.</div>
  <div class="abs small" style="left:345px;top:92px;width:120px;text-align:center"><div class="label">Your Contents Here</div>Lorem ipsum dolor sit amet, consectetur adipiscing elit, sed do eiusmod tempor incididunt ut labore et dolore magna aliqua.</div>
  <svg class="abs" style="left:0;top:140px" width="626" height="140">
    <g fill="none" stroke-width="14">
      <path d="M62 72 A48 48 0 0 0 158 72" stroke="var(--cyan)"/>
      <path d="M160 72 A48 48 0 0 1 256 72" stroke="var(--cyan-light)"/>
      <path d="M258 72 A48 48 0 0 0 354 72" stroke="var(--cyan)"/>
      <path d="M356 72 A48 48 0 0 1 452 72" stroke="var(--cyan-light)"/>
      <path d="M454 72 A48 48 0 0 0 550 72" stroke="var(--cyan)"/>
    </g>
    <g stroke="#fff" stroke-width="3">
      <circle cx="110" cy="72" r="30" fill="var(--cyan)"/><circle cx="208" cy="72" r="30" fill="#c4eaf9"/>
      <circle cx="306" cy="72" r="30" fill="var(--cyan)"/><circle cx="404" cy="72" r="30" fill="#c4eaf9"/>
      <circle cx="502" cy="72" r="30" fill="var(--cyan)"/>
    </g>
    <g fill="#fff">
      <circle cx="110" cy="68" r="7"/><rect x="106" y="75" width="8" height="5"/>
      <circle cx="208" cy="72" r="11" fill="none" stroke="#fff" stroke-width="2"/><circle cx="208" cy="72" r="4"/>
      <path d="M294 74 H318 L314 82 H298 Z"/><rect x="300" y="64" width="12" height="8"/>
      <path d="M392 76 L416 66 L418 70 L404 76 L410 84 L406 85 L398 78 L392 80 Z"/>
      <path d="M490 72 L498 64 L506 70 L514 64 L514 76 L504 82 Z"/>
    </g>
  </svg>
  <div class="abs small" style="left:45px;top:274px;width:130px;text-align:center"><div class="label">Your Contents Here</div>Lorem ipsum dolor sit amet, consectetur adipiscing elit, sed do eiusmod tempor incididunt ut labore et dolore magna aliqua.</div>
  <div class="abs small" style="left:245px;top:274px;width:130px;text-align:center"><div class="label">Your Contents Here</div>Lorem ipsum dolor sit amet, consectetur adipiscing elit, sed do eiusmod tempor incididunt ut labore et dolore magna aliqua.</div>
  <div class="abs small" style="left:438px;top:274px;width:130px;text-align:center"><div class="label">Your Contents Here</div>Lorem ipsum dolor sit amet, consectetur adipiscing elit, sed do eiusmod tempor incididunt ut labore et dolore magna aliqua.</div>
</section>

<!-- 9 Our team -->
<section class="slide c3 r3">
  <div class="head-rule"></div><div class="tab"></div><div class="mark"><i></i>MERIDEX</div>
  <div class="title" style="top:26px;font-size:28px">Our Team</div>
  <div class="abs" style="left:0;top:82px;width:626px;height:90px;background:var(--cyan)"></div>
  <div class="photo" role="img" aria-label="Team member portrait" style="left:92px;top:75px;width:104px;height:104px;background:linear-gradient(180deg,#d9d9d9,#9a9a9a)"></div>
  <div class="photo" role="img" aria-label="Team member portrait" style="left:209px;top:75px;width:104px;height:104px;background:linear-gradient(180deg,#e4e4e4,#8f8f8f)"></div>
  <div class="photo" role="img" aria-label="Team member portrait" style="left:326px;top:75px;width:104px;height:104px;background:linear-gradient(180deg,#cfcfcf,#8a8a8a)"></div>
  <div class="photo" role="img" aria-label="Team member portrait" style="left:443px;top:75px;width:104px;height:104px;background:linear-gradient(180deg,#efefef,#a8a8a8)"></div>
  <div class="abs" style="left:92px;top:192px;width:100px"><div style="font-size:10px;font-weight:700;color:#1d3a5a">Joe Doe</div><div style="font-size:10px;color:var(--cyan-deep)">Lorem Ipsum</div><div class="small" style="margin-top:12px">Lorem ipsum dolor sit amet, consectetur adipiscing elit. Morbi facilisis tellus.</div><div style="width:14px;height:1px;background:var(--cyan);margin-top:12px"></div></div>
  <div class="abs" style="left:209px;top:192px;width:100px"><div style="font-size:10px;font-weight:700;color:#1d3a5a">Jhon Dan</div><div style="font-size:10px;color:var(--cyan-deep)">Lorem Ipsum</div><div class="small" style="margin-top:12px">Lorem ipsum dolor sit amet, consectetur adipiscing elit. Morbi facilisis tellus.</div><div style="width:14px;height:1px;background:var(--cyan);margin-top:12px"></div></div>
  <div class="abs" style="left:326px;top:192px;width:100px"><div style="font-size:10px;font-weight:700;color:#1d3a5a">James Min</div><div style="font-size:10px;color:var(--cyan-deep)">Lorem Ipsum</div><div class="small" style="margin-top:12px">Lorem ipsum dolor sit amet, consectetur adipiscing elit. Morbi facilisis tellus.</div><div style="width:14px;height:1px;background:var(--cyan);margin-top:12px"></div></div>
  <div class="abs" style="left:443px;top:192px;width:100px"><div style="font-size:10px;font-weight:700;color:#1d3a5a">Veronica Jas</div><div style="font-size:10px;color:var(--cyan-deep)">Lorem Ipsum</div><div class="small" style="margin-top:12px">Lorem ipsum dolor sit amet, consectetur adipiscing elit. Morbi facilisis tellus.</div><div style="width:14px;height:1px;background:var(--cyan);margin-top:12px"></div></div>
</section>

<!-- 10 Three modes -->
<section class="slide c1 r4">
  <div class="head-rule"></div><div class="tab"></div><div class="mark"><i></i>MERIDEX</div>
  <div class="abs" style="left:0;width:620px;top:42px;text-align:center;font-size:22px;font-weight:700">Lorem ipsum dolor sit amet</div>
  <svg class="abs" style="left:0;top:70px" width="340" height="270">
    <g fill="none" stroke="var(--cyan)" stroke-width="1.5">
      <path d="M40 120 A65 65 0 1 0 120 115"/>
      <path d="M230 115 A65 65 0 1 0 300 120"/>
    </g>
    <path d="M122 115 A62 62 0 1 1 228 115" fill="none" stroke="var(--cyan)" stroke-width="22"/>
    <g fill="var(--cyan)" stroke="#fff" stroke-width="3">
      <circle cx="175" cy="78" r="30"/><circle cx="82" cy="172" r="30"/><circle cx="270" cy="172" r="30"/>
    </g>
    <g fill="#fff">
      <path d="M162 82 L188 70 L190 74 L176 80 L182 90 L178 91 L170 83 L162 85 Z"/>
      <rect x="70" y="166" width="24" height="10" rx="3"/><circle cx="75" cy="179" r="3"/><circle cx="89" cy="179" r="3"/>
      <path d="M256 174 H284 L279 182 H261 Z"/><rect x="263" y="164" width="14" height="9"/>
    </g>
  </svg>
  <div class="abs" style="left:355px;top:84px;width:4px;height:58px;background:var(--cyan)"></div>
  <div class="abs" style="left:372px;top:84px;width:200px;font-size:8px;line-height:1.5;color:#333"><b>Your Text Here</b><br>You can simply impress your audience and add a unique zing and appeal to your Presentations.</div>
  <div class="abs" style="left:355px;top:166px;width:4px;height:58px;background:var(--cyan)"></div>
  <div class="abs" style="left:372px;top:166px;width:200px;font-size:8px;line-height:1.5;color:#333"><b>Your Text Here</b><br>You can simply impress your audience and add a unique zing and appeal to your Presentations.</div>
  <div class="abs" style="left:355px;top:248px;width:4px;height:58px;background:var(--cyan)"></div>
  <div class="abs" style="left:372px;top:248px;width:200px;font-size:8px;line-height:1.5;color:#333"><b>Your Text Here</b><br>You can simply impress your audience and add a unique zing and appeal to your Presentations.</div>
</section>

<!-- 11 Map with checks -->
<section class="slide c2 r4">
  <div class="head-rule"></div><div class="tab"></div><div class="mark"><i></i>MERIDEX</div>
  <div class="title" style="top:42px">Lorem ipsum dolor sit amet</div>
  <div class="abs small just" style="left:38px;top:100px;width:222px;font-size:8px"><p style="margin:0 0 10px">Lorem ipsum dolor sit amet, consectetur adipiscing elit, sed do eiusmod tempor incididunt ut labore et dolore magna aliqua. Lorem ipsum dolor sit amet, consectetur adipiscing elit, sed do eiusmod tempor incididunt ut labore et dolore magna aliqua.</p><p style="margin:0">Lorem ipsum dolor sit amet, consectetur adipiscing elit, sed do eiusmod tempor incididunt ut labore et dolore magna aliqua. Lorem ipsum dolor sit amet, consectetur adipiscing elit, sed do eiusmod tempor incididunt ut labore et dolore magna aliqua. Lorem ipsum dolor sit amet, consectetur adipiscing elit, sed do eiusmod tempor incididunt ut labore et dolore magna aliqua.</p></div>
  <div class="photo" role="img" aria-label="World map in light blue" style="left:270px;top:90px;width:250px;height:230px;border-radius:45%;background:radial-gradient(circle,rgba(41,181,232,.35),rgba(41,181,232,.08) 70%,transparent)"></div>
  <svg class="abs" style="left:320px;top:100px" width="30" height="230">
    <g stroke="#fff" stroke-width="2.5" fill="none">
      <circle cx="15" cy="18" r="15" fill="#b5b5b5" stroke="none"/><path d="M8 18 L13 23 L22 13"/>
      <circle cx="15" cy="80" r="15" fill="var(--cyan)" stroke="none"/><path d="M8 80 L13 85 L22 75"/>
      <circle cx="15" cy="142" r="15" fill="#b5b5b5" stroke="none"/><path d="M8 142 L13 147 L22 137"/>
      <circle cx="15" cy="204" r="15" fill="var(--cyan)" stroke="none"/><path d="M8 204 L13 209 L22 199"/>
    </g>
  </svg>
  <div class="abs small" style="left:368px;top:100px;width:150px"><div class="label">Lorem ipsum dolor</div>Lorem ipsum dolor sit amet, consectetur adipiscing elit, sed do eiusmod tempor</div>
  <div class="abs small" style="left:368px;top:162px;width:150px"><div class="label">Lorem ipsum dolor</div>Lorem ipsum dolor sit amet, consectetur adipiscing elit, sed do eiusmod tempor</div>
  <div class="abs small" style="left:368px;top:224px;width:150px"><div class="label">Lorem ipsum dolor</div>Lorem ipsum dolor sit amet, consectetur adipiscing elit, sed do eiusmod tempor</div>
  <div class="abs small" style="left:368px;top:286px;width:150px"><div class="label">Lorem ipsum dolor</div>Lorem ipsum dolor sit amet, consectetur adipiscing elit, sed do eiusmod tempor</div>
</section>

<!-- 12 Idea / developer / business -->
<section class="slide c3 r4">
  <div class="photo" role="img" aria-label="Business person working at a laptop" style="left:0;top:0;width:626px;height:168px;background:linear-gradient(90deg,#2a3a55 0%,#6fa7cf 35%,#4cc0ee 65%,#29b5e8 100%)"></div>
  <div class="abs" style="right:20px;top:22px;font-family:'Open Sans',Arial,sans-serif;font-size:24px;font-weight:600;color:#fff">Lorem ipsum dolor sit amet</div>
  <div class="abs" style="right:20px;top:64px;width:340px;text-align:right;font-size:8px;line-height:1.5;color:#fff">Lorem ipsum dolor sit amet, consectetur adipiscing elit, sed do eiusmod tempor incididunt ut labore et dolore magna aliqua. Ut enim ad minim veniam, quis nostrud exercitation ullamco laboris nisi ut aliquip ex ea commodo consequat.</div>
  <svg class="abs" style="left:140px;top:190px" width="340" height="75">
    <g stroke="var(--cyan)" stroke-width="1.5">
      <rect x="23" y="13" width="46" height="46" rx="12" transform="rotate(45 46 36)" fill="#fff"/>
      <rect x="139" y="13" width="46" height="46" rx="12" transform="rotate(45 162 36)" fill="var(--cyan)"/>
      <rect x="255" y="13" width="46" height="46" rx="12" transform="rotate(45 278 36)" fill="#fff"/>
    </g>
    <path d="M36 40 L56 28 L50 48 L46 40 Z" fill="none" stroke="var(--cyan)" stroke-width="1.5"/>
    <circle cx="162" cy="36" r="8" fill="none" stroke="#fff" stroke-width="2"/><circle cx="162" cy="36" r="3" fill="#fff"/>
    <rect x="270" y="30" width="16" height="12" fill="none" stroke="var(--cyan)" stroke-width="1.5"/><rect x="274" y="26" width="8" height="4" fill="none" stroke="var(--cyan)" stroke-width="1.5"/>
  </svg>
  <div class="abs" style="left:136px;top:272px;width:100px;text-align:center;font-size:7.5px;font-weight:700;letter-spacing:1px">IDEA</div>
  <div class="abs" style="left:252px;top:272px;width:100px;text-align:center;font-size:7.5px;font-weight:700;letter-spacing:1px">DEVELOPER</div>
  <div class="abs" style="left:368px;top:272px;width:100px;text-align:center;font-size:7.5px;font-weight:700;letter-spacing:1px">BUSINESS</div>
  <div class="abs" style="left:131px;top:292px;width:110px;text-align:center;font-size:6.5px;line-height:1.4;color:#333">Sed ut perspiciatis, unde omnis iste natus error sit voluptatem accusantium</div>
  <div class="abs" style="left:247px;top:292px;width:110px;text-align:center;font-size:6.5px;line-height:1.4;color:#333">Sed ut perspiciatis, unde omnis iste natus error sit voluptatem accusantium</div>
  <div class="abs" style="left:363px;top:292px;width:110px;text-align:center;font-size:6.5px;line-height:1.4;color:#333">Sed ut perspiciatis, unde omnis iste natus error sit voluptatem accusantium</div>
</section>

<!-- 13 Three text columns -->
<section class="slide c1 r5">
  <div class="head-rule"></div><div class="tab"></div><div class="mark"><i></i>MERIDEX</div>
  <div class="abs" style="left:0;width:620px;top:32px;text-align:center;font-size:22px;font-weight:700">Lorem ipsum dolor sit amet</div>
  <div class="abs just" style="left:50px;top:80px;width:150px;font-size:7.5px;line-height:1.45;color:#333">Lorem ipsum dolor sit amet, consectetur adipiscing elit, sed do eiusmod tempor incididunt ut labore et dolore magna aliqua. Ut enim ad minim veniam, quis nostrud exercitation ullamco aliquip ex ea commodo consequat. Lorem ipsum dolor sit amet, consectetur adipiscing elit, sed do eiusmod tempor incididunt ut labore et dolore magna aliqua. Lorem ipsum dolor sit amet, consectetur adipiscing elit, sed do eiusmod tempor ut labore et dolore magna aliqua. Ut enim ad minim veniam, quis nostrud exercitation ullamco laboris nisi ut aliquip ex ea commodo.</div>
  <div class="abs just" style="left:232px;top:80px;width:150px;font-size:7.5px;line-height:1.45;color:#333">Lorem ipsum dolor sit amet, consectetur adipiscing elit, sed do eiusmod tempor incididunt ut labore et dolore magna aliqua. Ut enim ad minim veniam, quis nostrud exercitation ullamco laboris nisi ut aliquip ex ea commodo consequat. Lorem ipsum dolor sit amet, consectetur adipiscing elit, sed do eiusmod tempor incididunt ut labore et dolore magna aliqua.<br><br>Ut enim ad minim veniam, quis nostrud exercitation ullamco laboris nisi ut aliquip ex ea commodo consequat, consectetur adipiscing elit, sed do eiusmod tempor incididunt ut labore et dolore magna aliqua.</div>
  <div class="abs just" style="left:420px;top:80px;width:155px;font-size:7.5px;line-height:1.45;color:#333">Lorem ipsum dolor sit amet, consectetur adipiscing elit, sed do eiusmod tempor incididunt ut labore et dolore magna aliqua. Ut enim ad minim veniam, quis nostrud exercitation ullamco aliquip ex ea commodo consequat. Lorem ipsum dolor sit amet, consectetur adipiscing elit, sed do eiusmod tempor incididunt ut labore et dolore magna aliqua. Lorem ipsum dolor sit amet, consectetur adipiscing elit, sed do eiusmod tempor ut labore et dolore magna aliqua. Ut enim ad minim veniam, quis nostrud exercitation ullamco laboris nisi ut aliquip ex ea commodo consequat. Lorem ipsum dolor sit amet, consectetur adipiscing elit, sed do eiusmod tempor incididunt ut labore et dolore magna aliqua.</div>
</section>

<!-- 14 Get in touch -->
<section class="slide c2 r5" style="background:linear-gradient(160deg,#2fb3e6 0%,#5ec8f0 60%,#9fdcf5 100%)">
  <svg class="abs" style="left:0;top:0" width="626" height="352"><path d="M626 80 L626 352 L360 352 C470 300 560 200 626 80 Z" fill="#fff"/></svg>
  <div class="abs" style="left:0;right:0;top:26px;text-align:center;font-family:'Open Sans',Arial,sans-serif;font-size:28px;font-weight:600;color:#fff">Get in Touch</div>
  <div class="abs" style="left:0;right:0;top:62px;text-align:center;font-size:7.5px;color:#fff">Lorem ipsum dolor sit amet, consectetur adipiscing elit, sed do eiusmod tempor incididunt ut labore et dolore magna aliqua.</div>
  <svg class="abs" style="left:50px;top:112px" width="40" height="190" fill="none" stroke="#fff" stroke-width="2">
    <circle cx="16" cy="18" r="13"/><ellipse cx="16" cy="18" rx="6" ry="13"/><line x1="3" y1="18" x2="29" y2="18"/>
    <path d="M8 64 C8 80 18 90 28 90 L30 84 L24 80 L20 83 C16 81 13 77 12 73 L15 70 L12 64 Z" fill="#fff" stroke="none"/>
    <rect x="3" y="122" width="28" height="20" rx="2" fill="#fff" stroke="none"/><path d="M4 124 L17 134 L30 124" stroke="var(--cyan)"/>
    <path d="M17 190 C9 178 7 174 7 168 A10 10 0 0 1 27 168 C27 174 25 178 17 190 Z" fill="#fff" stroke="none"/><circle cx="17" cy="168" r="3.5" fill="var(--cyan)" stroke="none"/>
  </svg>
  <div class="abs" style="left:116px;top:122px;font-size:8px;color:#fff">www.website.com</div>
  <div class="abs" style="left:116px;top:176px;font-size:8px;color:#fff">555.010.2048</div>
  <div class="abs" style="left:118px;top:228px;font-size:8px;color:#fff">info@website.com</div>
  <div class="abs" style="left:116px;top:280px;font-size:8px;line-height:1.4;color:#fff">Here to write your,<br>Company adress</div>
  <div class="photo" role="img" aria-label="Aircraft and trucks at an airport in greyscale" style="left:258px;top:132px;width:340px;height:218px;border-radius:55% 45% 50% 50% / 55% 60% 40% 45%;background:linear-gradient(160deg,#d9d9d9,#7a7a7a 55%,#3c3c3c)"></div>
  <div class="abs" style="left:320px;top:226px">
    <div class="brand" style="font-size:26px"><i style="width:15px;height:15px"></i>MERIDEX</div>
  </div>
</section>

</body>
</html>
```